Letterhead design x 2, follower page, with compliments slip and envelope design X 2

Design letterhead x 2, follower page, with compliments slip and envelope x 2 for Harbourline Trade Advisors, a business broking company. Using the colours of the existing logo and a white background for a clean, sophisticated look.

Target Market(s)

Family Business owners and regular business owners looking to buy or sell their business, or improve the value of their business.

Font styles to use
Sans Serif

Requirements
Must have
• Letterhead design 1 - Additional logos for Torvald Trade Exchange, QLMR and HCX to be included in a small size somewhere on the page. Torvald Trade Exchange logo only to have the wording 'Powered By' alongside. Please do not distort the size of the logos.
Letterhead design 2 - Additional logos for QLMR and HCX to be included in a small size somewhere on the page. This design will not include the Torvald Trade Exchange logo or the words 'Powered By'. Please do not distort the size of the logos.
Envelope design 1 - Please include an address window
Envelope design 2 - Do not include an address window

```html
<!DOCTYPE html>
<html lang="en">
<head>
<meta charset="utf-8">
<title>Harbourline Trade Advisors – Stationery Set</title>
<link href="https://fonts.googleapis.com/css2?family=Poppins:wght@400;500;600&family=Lato:wght@400&family=Great+Vibes&display=swap" rel="stylesheet">
<style>
:root{
  --stage:#a7a6a7;
  --paper:#f4f3f1;
  --brand:#f15a2b;
  --ink:#5b5b5b;
  --soft:#7a7a7a;
  --mark:#e6e4e2;
  --window:#c9c9c9;
  --navy:#1f3a6b;
}
*{box-sizing:border-box;margin:0;padding:0}
html,body{width:1032px;height:1200px;overflow:hidden;background:var(--stage)}
body{position:relative;font-family:'Poppins',sans-serif;color:var(--ink)}
.sheet{position:absolute;background:var(--paper);overflow:hidden;box-shadow:0 2px 6px rgba(0,0,0,.25)}
.sheet::before{content:"";position:absolute;left:0;top:0;bottom:0;width:6px;background:var(--brand)}
.letter{width:438px;height:619px}
.envelope{width:445px;height:202px}
.label{position:absolute;font:600 9px 'Poppins',sans-serif;color:#222;letter-spacing:.5px;text-align:center}
.faint-ring{position:absolute;border:9px solid var(--mark);border-radius:50%;opacity:.7}
.brand{position:absolute;display:flex;align-items:center;gap:8px}
.brand-ring{border:2px solid #8d8d8d;border-radius:50%;flex:none}
.brand-name{font-weight:500;color:var(--brand);line-height:1.02}
.contact{position:absolute;border-left:1px solid #777;padding-left:11px;font-size:7.4px;line-height:9.3px;color:var(--ink)}
.contact svg{width:7px;height:7px;vertical-align:-1px;margin-right:3px}
.greeting{position:absolute;left:54px;top:180px;font:400 11.5px 'Lato',sans-serif;color:#555}
.body-copy{position:absolute;left:54px;top:214px;width:342px;font:400 5.9px/10.6px 'Lato',sans-serif;color:#666}
.body-copy p{margin-bottom:10.6px}
.sign-off{position:absolute;left:54px;top:432px;font:400 6px 'Lato',sans-serif;color:#666}
.signature{position:absolute;left:53px;top:448px;width:56px;height:14px;background:#d9d8d6}
.partner{position:absolute;top:576px;display:flex;align-items:center;gap:4px}
.powered{font:400 4px 'Poppins',sans-serif;color:#222;line-height:5px}
.powered b{display:block;font-weight:600;font-size:5px;letter-spacing:.3px}
.qlmr{font:600 10px 'Poppins',sans-serif;color:var(--navy);letter-spacing:1.5px}
.qlmr-dot{width:14px;height:14px;border-radius:50%;background:var(--navy)}
.badge{position:absolute;top:576px;width:28px;height:28px;border-radius:50%;border:2px solid #3a5a9c;background:#e9eef7}
.return-address{position:absolute;left:25px;top:78px;font-size:7.4px;line-height:8.8px}
.window{position:absolute;left:235px;top:102px;width:180px;height:72px;border-radius:8px;background:var(--window);border:1px solid #b8b8b8}
.flap{position:absolute;left:0;right:0;top:0;height:63px;background:var(--brand);border-radius:0 0 22px 22px}
.flap-brand{position:absolute;left:50%;top:15px;transform:translateX(-50%);display:flex;align-items:center;gap:5px;color:#fff;font-size:8px;font-weight:500}
.flap-brand i{width:22px;height:22px;border:2px solid #fff;border-radius:50%}
.slip-line{position:absolute;left:25px;font-size:7.4px;white-space:nowrap}
.slip-line svg{width:7px;height:7px;vertical-align:-1px;margin:0 2px 0 0}
.compliments{position:absolute;right:32px;top:130px;font:400 27px 'Great Vibes',cursive;color:var(--brand);border-bottom:1px solid var(--brand);line-height:28px;padding:0 2px}
</style>
</head>
<body>
<svg width="0" height="0" style="position:absolute">
  <symbol id="i-phone" viewBox="0 0 10 10"><path fill="#f15a2b" d="M2 .5l2 2-1 1.3a6 6 0 003.2 3.2L7.5 6l2 2-1.3 1.5C4.5 9.3.7 5.5.5 1.8z"/></symbol>
  <symbol id="i-fax" viewBox="0 0 10 10"><rect fill="#f15a2b" x="2.5" y="0.5" width="5" height="3"/><rect fill="#f15a2b" x="0.5" y="3.5" width="9" height="4.5" rx="1"/><rect fill="#f15a2b" x="2.5" y="7" width="5" height="2.5"/></symbol>
  <symbol id="i-mail" viewBox="0 0 10 10"><rect fill="#f15a2b" x="0.5" y="2" width="9" height="6.5"/><path d="M.5 2l4.5 3.5L9.5 2" stroke="#fff" fill="none"/></symbol>
  <symbol id="i-web" viewBox="0 0 10 10"><circle cx="5" cy="5" r="4.5" fill="#f15a2b"/><path d="M.5 5h9M5 .5c2 2.5 2 6.5 0 9M5 .5c-2 2.5-2 6.5 0 9" stroke="#fff" stroke-width=".7" fill="none"/></symbol>
</svg>

<!-- Letterhead 1 -->
<section class="sheet letter" style="left:53px;top:42px">
  <div class="faint-ring" style="left:103px;top:170px;width:280px;height:280px"></div>
  <div class="brand" style="left:41px;top:48px"><span class="brand-ring" style="width:44px;height:44px"></span><span class="brand-name" style="font-size:13.5px">Harbourline<br>Trade<br>Advisors</span></div>
  <address class="contact" style="left:286px;top:40px;font-style:normal">214 Keelson Street<br>Portmead, Oregon 97412<br><svg><use href="#i-phone"/></svg>503 218 4470<br><svg><use href="#i-fax"/></svg>503 218 4471<br><svg><use href="#i-mail"/></svg>hello@harbourline.co<br><svg><use href="#i-web"/></svg>www.harbourline.co</address>
  <p class="greeting">Dear Mr. Hale,</p>
  <div class="body-copy">
    <p>Lorem ipsum dolor sit amet, consectetur adipiscing elit. Donec orci purus, luctus vitae dignissim eu, iaculis sed purus. Vivamus faucibus, ipsum nec aliquet viverra, leo mauris condimentum ligula, sit amet sagittis enim ligula quis arcu. Nam egestas tortor id nisi porttitor mattis. In tortor ante, ultricies in suscipit a, tempus non massa. Vivamus et auctor mi. Fusce vel massa nulla. Phasellus nec eros mauris, et scelerisque orci.</p>
    <p>Donec malesuada orci vitae nulla accumsan porta a id massa. Quisque accumsan iaculis magna sit amet fringilla. Maecenas consequat, magna eget tincidunt semper, odio nibh rutrum mi, id feugiat ante nisi eu risus. Vestibulum nunc orci, rhoncus a placerat in, ultricies in mi. Cras mattis varius eros, vel fringilla nisi suscipit eget. Quisque scelerisque sagittis nulla at porttitor.</p>
    <p>Sed id augue vitae urna euismod commodo aliquet a quam. Pellentesque arcu velit, cursus et malesuada ut, consequat et diam. Nullam erat sem, rhoncus id ullamcorper vitae, rhoncus et arcu. In ultricies ultricies nulla, ut rutrum nisi iaculis at. Donec eu magna a metus ornare faucibus. Fusce aliquet faucibus ultricies. Morbi semper, est id tincidunt gravida, sem arcu adipiscing lacus, ac bibendum nulla leo eu purus. Quisque nec diam sed risus consectetur a cumsan quis quis nibh. Vestibulum id purus lorem.</p>
    <p>It is a long established fact that a reader will be distracted by the readable content of a page when looking at its layout. The point of using Lorem Ipsum is that it has a more-or-less normal distribution of letters, as opposed to using 'Content here, content here', making it look like readable English. Many desktop publishing packages</p>
  </div>
  <p class="sign-off">Sincerely,</p>
  <div class="signature" role="img" aria-label="Handwritten signature"></div>
  <div class="partner" style="left:42px;top:584px"><span class="powered">Powered By<b>Torvald Trade Exchange</b></span></div>
  <div class="partner" style="left:193px;top:584px"><span class="qlmr-dot"></span><span class="qlmr">QLMR</span></div>
  <span class="badge" style="left:368px" role="img" aria-label="HCX member badge"></span>
</section>
<p class="label" style="left:53px;top:672px;width:438px">LETTER_01</p>

<!-- Letterhead 2 -->
<section class="sheet letter" style="left:528px;top:41px">
  <div class="faint-ring" style="left:103px;top:170px;width:280px;height:280px"></div>
  <div class="brand" style="left:41px;top:48px"><span class="brand-ring" style="width:44px;height:44px"></span><span class="brand-name" style="font-size:13.5px">Harbourline<br>Trade<br>Advisors</span></div>
  <address class="contact" style="left:286px;top:40px;font-style:normal">214 Keelson Street<br>Portmead, Oregon 97412<br><svg><use href="#i-phone"/></svg>503 218 4470<br><svg><use href="#i-fax"/></svg>503 218 4471<br><svg><use href="#i-mail"/></svg>hello@harbourline.co<br><svg><use href="#i-web"/></svg>www.harbourline.co</address>
  <p class="greeting">Dear Mr. Hale,</p>
  <div class="body-copy">
    <p>Lorem ipsum dolor sit amet, consectetur adipiscing elit. Donec orci purus, luctus vitae dignissim eu, iaculis sed purus. Vivamus faucibus, ipsum nec aliquet viverra, leo mauris condimentum ligula, sit amet sagittis enim ligula quis arcu. Nam egestas tortor id nisi porttitor mattis. In tortor ante, ultricies in suscipit a, tempus non massa. Vivamus et auctor mi. Fusce vel massa nulla. Phasellus nec eros mauris, et scelerisque orci.</p>
    <p>Donec malesuada orci vitae nulla accumsan porta a id massa. Quisque accumsan iaculis magna sit amet fringilla. Maecenas consequat, magna eget tincidunt semper, odio nibh rutrum mi, id feugiat ante nisi eu risus. Vestibulum nunc orci, rhoncus a placerat in, ultricies in mi. Cras mattis varius eros, vel fringilla nisi suscipit eget. Quisque scelerisque sagittis nulla at porttitor.</p>
    <p>Sed id augue vitae urna euismod commodo aliquet a quam. Pellentesque arcu velit, cursus et malesuada ut, consequat et diam. Nullam erat sem, rhoncus id ullamcorper vitae, rhoncus et arcu. In ultricies ultricies nulla, ut rutrum nisi iaculis at. Donec eu magna a metus ornare faucibus. Fusce aliquet faucibus ultricies. Morbi semper, est id tincidunt gravida, sem arcu adipiscing lacus, ac bibendum nulla leo eu purus. Quisque nec diam sed risus consectetur a cumsan quis quis nibh. Vestibulum id purus lorem.</p>
    <p>It is a long established fact that a reader will be distracted by the readable content of a page when looking at its layout. The point of using Lorem Ipsum is that it has a more-or-less normal distribution of letters, as opposed to using 'Content here, content here', making it look like readable English. Many desktop publishing packages</p>
  </div>
  <p class="sign-off">Sincerely,</p>
  <div class="signature" role="img" aria-label="Handwritten signature"></div>
  <div class="partner" style="left:44px;top:584px"><span class="qlmr-dot"></span><span class="qlmr">QLMR</span></div>
  <span class="badge" style="left:368px" role="img" aria-label="HCX member badge"></span>
</section>
<p class="label" style="left:528px;top:672px;width:438px">LETTER_02</p>

<!-- Envelope front 1 -->
<section class="sheet envelope" style="left:53px;top:700px">
  <div class="faint-ring" style="left:257px;top:20px;width:164px;height:164px"></div>
  <div class="brand" style="left:27px;top:26px"><span class="brand-ring" style="width:38px;height:38px"></span><span class="brand-name" style="font-size:12px">Harbourline<br>Trade<br>Advisors</span></div>
  <p class="return-address">214 Keelson Street<br>Portmead, Oregon 97412</p>
</section>
<p class="label" style="left:53px;top:914px;width:445px">ENVELOPE FRONT_01</p>

<!-- Envelope back -->
<section class="sheet envelope" style="left:526px;top:701px;width:444px">
  <div class="flap"><span class="flap-brand"><i></i>Harbourline</span></div>
</section>
<p class="label" style="left:526px;top:914px;width:444px">ENVELOPE BACK_01</p>

<!-- Envelope front 2 -->
<section class="sheet envelope" style="left:53px;top:944px">
  <div class="faint-ring" style="left:257px;top:20px;width:164px;height:164px"></div>
  <div class="brand" style="left:27px;top:26px"><span class="brand-ring" style="width:38px;height:38px"></span><span class="brand-name" style="font-size:12px">Harbourline<br>Trade<br>Advisors</span></div>
  <p class="return-address">214 Keelson Street<br>Portmead, Oregon 97412</p>
  <div class="window"></div>
</section>
<p class="label" style="left:53px;top:1160px;width:445px">ENVELOPE FRONT_02</p>

<!-- Compliment slip -->
<section class="sheet envelope" style="left:526px;top:944px;width:446px">
  <div class="faint-ring" style="left:268px;top:20px;width:160px;height:160px"></div>
  <div class="brand" style="left:21px;top:24px"><span class="brand-ring" style="width:38px;height:38px"></span><span class="brand-name" style="font-size:12px">Harbourline<br>Trade<br>Advisors</span></div>
  <p class="compliments">With Compliments</p>
  <p class="slip-line" style="top:157px">214 Keelson Street, Portmead, Oregon 97412</p>
  <p class="slip-line" style="top:171px"><svg><use href="#i-phone"/></svg>503 218 4470 <svg><use href="#i-fax"/></svg>503 218 4471 <svg><use href="#i-mail"/></svg>hello@harbourline.co <svg><use href="#i-web"/></svg>www.harbourline.co</p>
</section>
<p class="label" style="left:526px;top:1160px;width:446px">COMPLIMENT SLIP</p>
</body>
</html>
```